Laser Hair Removal Tri Fold brochure

I'm looking for a tri fold brochure (A4 size) for a cosmetic surgery centre / dermatology clinic for our laser hair removal services please.

Whilst we are more medical centre than spa, and cater to both men and women, some warmth would good to convey.

I've attached several versions of our logo - either can be used depending on the design style and colouring used. You can see more about us at www.qentrava.ae. I've also added some photos of our clinic if that is of any interest. No need to use them but they're there if you want them.

As we are based in the Middle East, no images showing too much skin should be used. Legs or face, or certain parts of the body are fine, so long as they aren't too revealing, as we need to be culturally sensitive.

One of our (non creative) staff has drafted a basic brochure using Word, which I've attached as a point of reference or for content, although naturally it's not professionally done so it's by no means a design guide! Also open to written content improvement if necessary but this part is non-essential. The only content I specifically want to keep is the price list please.

Many thanks!

Clinic

```html
<!DOCTYPE html>
<html lang="en">
<head>
<meta charset="utf-8">
<title>Laser Hair Removal – Qentrava Aesthetics Clinic</title>
<link href="https://fonts.googleapis.com/css2?family=Open+Sans:wght@400;600;700&family=Yellowtail&display=swap" rel="stylesheet">
<style>
  :root {
    --panel-pink: #f7bdea;
    --ink: #2e2e2e;
    --magenta-light: #d46ccb;
    --magenta: #b33aa8;
    --magenta-deep: #960f8c;
    --photo-light: #efe4dc;
    --photo-mid: #d9c4b4;
    --wave-pink: #f0a7e2;
    --ornament: #e7a3dc;
    --white: #ffffff;
  }
  * { margin: 0; padding: 0; box-sizing: border-box; }
  html, body { width: 1200px; height: 848px; overflow: hidden; background: #ffffff; }
  .brochure {
    position: relative;
    width: 1200px;
    height: 848px;
    font-family: "Open Sans", Arial, sans-serif;
    color: var(--ink);
    background: var(--panel-pink);
    overflow: hidden;
  }
  .price-list {
    position: absolute;
    left: 36px;
    top: 11px;
    width: 330px;
  }
  .price-list__title {
    font-size: 17px;
    font-weight: 400;
    line-height: 22px;
    margin-bottom: 36px;
  }
  .price-list__items { list-style: none; }
  .price-list__item {
    display: flex;
    font-size: 17px;
    line-height: 24px;
    height: 24px;
  }
  .price-list__area { width: 259px; }
  .contact {
    position: absolute;
    left: 470px;
    top: 494px;
    width: 250px;
    text-align: center;
    font-size: 12.5px;
    line-height: 21px;
    color: #222;
  }
  .contact__name, .contact__strong { font-weight: 700; }
  .ornament {
    position: absolute;
    left: 515px;
    top: 675px;
    width: 160px;
    height: 110px;
    border-radius: 50% 50% 40% 40%;
    background: radial-gradient(ellipse at center, var(--ornament) 0%, rgba(231,163,220,0.35) 55%, rgba(247,189,234,0) 75%);
  }
  .cover {
    position: absolute;
    left: 800px;
    top: 0;
    width: 400px;
    height: 848px;
    background: linear-gradient(180deg, var(--magenta-light) 0%, var(--magenta) 45%, var(--magenta-deep) 100%);
  }
  .cover__art { position: absolute; left: 0; top: 0; }
  .cover__brand {
    position: absolute;
    left: 0;
    top: 58px;
    width: 400px;
    text-align: center;
    font-size: 42px;
    font-weight: 600;
    letter-spacing: 2px;
    color: var(--white);
  }
  .cover__title {
    position: absolute;
    left: 0;
    top: 738px;
    width: 400px;
    text-align: center;
    font-family: "Yellowtail", cursive;
    font-size: 44px;
    color: var(--white);
  }
</style>
</head>
<body>
<main class="brochure">
  <section class="price-list">
    <h1 class="price-list__title">Laser Hair Removal Price List</h1>
    <ul class="price-list__items">
      <li class="price-list__item"><span class="price-list__area">Upper Lip</span><span>250</span></li>
      <li class="price-list__item"><span class="price-list__area">Back of Hands</span><span>480</span></li>
      <li class="price-list__item"><span class="price-list__area">Chin</span><span>300</span></li>
      <li class="price-list__item"><span class="price-list__area">Chin and Neck</span><span>550</span></li>
      <li class="price-list__item"><span class="price-list__area">Chin and Beard</span><span>500</span></li>
      <li class="price-list__item"><span class="price-list__area">Beard Definition</span><span>640</span></li>
      <li class="price-list__item"><span class="price-list__area">Neck &amp; Beard Definition</span><span>750</span></li>
      <li class="price-list__item"><span class="price-list__area">Full Beard</span><span>800</span></li>
      <li class="price-list__item"><span class="price-list__area">Lower Half Face</span><span>700</span></li>
      <li class="price-list__item"><span class="price-list__area">Lower Half Face and Neck</span><span>800</span></li>
      <li class="price-list__item"><span class="price-list__area">Full Face</span><span>850</span></li>
      <li class="price-list__item"><span class="price-list__area">Neck (Women)</span><span>320</span></li>
      <li class="price-list__item"><span class="price-list__area">Full Neck</span><span>680</span></li>
      <li class="price-list__item"><span class="price-list__area">Full Face and Neck</span><span>1000</span></li>
      <li class="price-list__item"><span class="price-list__area">Full Breast (Women)</span><span>300</span></li>
      <li class="price-list__item"><span class="price-list__area">Chest (Men)</span><span>1600</span></li>
      <li class="price-list__item"><span class="price-list__area">Buttocks</span><span>1040</span></li>
      <li class="price-list__item"><span class="price-list__area">Lower Back</span><span>1500</span></li>
      <li class="price-list__item"><span class="price-list__area">Upper Back</span><span>1500</span></li>
      <li class="price-list__item"><span class="price-list__area">Full Back</span><span>2000</span></li>
      <li class="price-list__item"><span class="price-list__area">Abdomen</span><span>1100</span></li>
      <li class="price-list__item"><span class="price-list__area">Underarms</span><span>600</span></li>
      <li class="price-list__item"><span class="price-list__area">Half Arms</span><span>880</span></li>
      <li class="price-list__item"><span class="price-list__area">Full Arms</span><span>1440</span></li>
      <li class="price-list__item"><span class="price-list__area">Half Legs</span><span>1800</span></li>
      <li class="price-list__item"><span class="price-list__area">Thighs</span><span>2100</span></li>
      <li class="price-list__item"><span class="price-list__area">Full Legs</span><span>2600</span></li>
      <li class="price-list__item"><span class="price-list__area">Bikini</span><span>650</span></li>
      <li class="price-list__item"><span class="price-list__area">Bikini + Underarm</span><span>1050</span></li>
      <li class="price-list__item"><span class="price-list__area">Full Bikini</span><span>1200</span></li>
      <li class="price-list__item"><span class="price-list__area">Full Bikini + Underarm</span><span>1600</span></li>
      <li class="price-list__item"><span class="price-list__area">Full Body</span><span>6400</span></li>
    </ul>
  </section>

  <address class="contact">
    <div class="contact__name">Qentrava Aesthetics Clinic</div>
    <div>Between 4th St (Marina)</div>
    <div>&amp; 9th St (Al Noor)</div>
    <div>Opposite Al Reem Garden Park</div>
    <div>PO BOX 540192</div>
    <div>Abu Dhabi, UAE</div>
    <div>T: <span class="contact__strong">+971 2 555 0148</span></div>
    <div>E: <span class="contact__strong">info@qentrava.ae</span></div>
  </address>

  <div class="ornament" role="img" aria-label="Decorative lotus flower ornament"></div>

  <section class="cover">
    <svg class="cover__art" width="400" height="848" viewBox="0 0 400 848">
      <defs>
        <linearGradient id="photoTone" x1="0" y1="0" x2="1" y2="1">
          <stop offset="0" stop-color="var(--photo-light)"/>
          <stop offset="0.6" stop-color="var(--photo-mid)"/>
          <stop offset="1" stop-color="#f3ece8"/>
        </linearGradient>
      </defs>
      <path d="M0,175 Q210,200 400,160 L400,185 Q200,215 0,192 Z" fill="var(--magenta-deep)" opacity="0.6"/>
      <path d="M0,695 Q200,730 400,680 L400,705 Q200,758 0,712 Z" fill="var(--wave-pink)"/>
      <path d="M0,185 Q210,208 400,172 L400,690 Q200,735 0,702 Z" fill="url(#photoTone)" role="img" aria-label="Photo of a client relaxing on a treatment bed during a laser hair removal session"/>
    </svg>
    <div class="cover__brand">QENTRAVA</div>
    <div class="cover__title">Laser Hair Removal</div>
  </section>
</main>
</body>
</html>
```